Brochure required

Looking at getting business brochure designed for my solar sales company. i will require a range of products to be listed on the brochure I require a simple/ elegent / professional looking brochure.

I am happy to provide designer with all the required information that must go into the brochure. otherwise please visit www.velorquintade.com.au and view the products which i would like to allocate into the brochure aswell as our company logo and a little about me section

```html
<!DOCTYPE html>
<html lang="en">
<head>
<meta charset="utf-8">
<title>Solar Products &amp; Services Brochure Spread</title>
<link href="https://fonts.googleapis.com/css2?family=Fira+Sans+Condensed:wght@400;600&display=swap" rel="stylesheet">
<style>
  :root {
    --page: #dcdcdc;
    --blue-deep: #0a6f9e;
    --blue-mid: #0995cf;
    --blue-bright: #12b3e6;
    --teal-band: #1aa3cf;
    --sky-pale: #c7d9ef;
    --white: #ffffff;
  }
  * { margin: 0; padding: 0; box-sizing: border-box; }
  html, body { width: 1200px; height: 996px; overflow: hidden; background: var(--page); }
  .brochure {
    position: relative; width: 1200px; height: 996px; overflow: hidden;
    font-family: "Fira Sans Condensed", "Arial Narrow", sans-serif;
    color: var(--white);
  }
  .brochure__backdrop { position: absolute; inset: 0; }
  .heading {
    position: absolute; left: 228px; top: 78px;
    font-size: 38px; font-weight: 600; text-decoration: underline;
    text-underline-offset: 5px; text-decoration-thickness: 2px;
  }
  .products { list-style: none; }
  .product {
    position: absolute; display: flex; align-items: center; gap: 14px;
    font-size: 32px; font-weight: 600; text-transform: uppercase;
  }
  .product__thumb {
    width: 76px; height: 72px; flex: none; position: relative;
    clip-path: polygon(25% 0, 75% 0, 100% 50%, 75% 100%, 25% 100%, 0 50%);
    background: var(--white);
  }
  .product__thumb span {
    position: absolute; inset: 3px;
    clip-path: polygon(25% 0, 75% 0, 100% 50%, 75% 100%, 25% 100%, 0 50%);
  }
  .product--inverters { left: 124px; top: 180px; }
  .product--batteries { left: 82px; top: 272px; }
  .product--panels { left: 44px; top: 364px; }
  .service__photo {
    position: absolute; width: 152px; height: 172px; border-radius: 50%;
    border: 5px solid var(--white);
  }
  .service__label {
    position: absolute; font-size: 34px; font-weight: 600; line-height: 1.12;
    text-transform: uppercase; text-align: center;
    text-shadow: 0 1px 3px rgba(0,0,0,0.35);
  }
  .client-photo {
    position: absolute; left: 1048px; top: 492px; width: 170px; height: 156px;
    clip-path: polygon(25% 0, 100% 0, 100% 100%, 25% 100%, 0 50%);
    background: var(--white);
  }
  .client-photo span {
    position: absolute; inset: 5px 0 5px 5px;
    clip-path: polygon(25% 0, 100% 0, 100% 100%, 25% 100%, 0 50%);
    background: linear-gradient(135deg, #8a8f99, #2c2f36);
  }
  .testimonial__name {
    position: absolute; right: 34px; top: 676px;
    font-size: 28px; font-weight: 600; text-decoration: underline;
    text-underline-offset: 4px; text-decoration-thickness: 2px;
  }
  .testimonial__quote {
    position: absolute; right: 30px; top: 720px; width: 320px;
    font-size: 21px; line-height: 1.28; text-align: right; font-weight: 400;
  }
</style>
</head>
<body>
<main class="brochure">
  <svg class="brochure__backdrop" width="1200" height="996" viewBox="0 0 1200 996">
    <defs>
      <linearGradient id="scene" x1="0" y1="0" x2="0" y2="1">
        <stop offset="0" stop-color="#b9cde6"/>
        <stop offset="0.38" stop-color="#c3d3e4"/>
        <stop offset="0.46" stop-color="#6f7b5c"/>
        <stop offset="0.55" stop-color="#566a86"/>
        <stop offset="1" stop-color="#3f4a76"/>
      </linearGradient>
      <linearGradient id="blueLeft" x1="0" y1="0" x2="1" y2="1">
        <stop offset="0" stop-color="#12b0e4"/>
        <stop offset="0.6" stop-color="#0a86bd"/>
        <stop offset="1" stop-color="#075f8e"/>
      </linearGradient>
      <linearGradient id="blueRight" x1="1" y1="0" x2="0" y2="1">
        <stop offset="0" stop-color="#1aa8df"/>
        <stop offset="1" stop-color="#0b7fb8"/>
      </linearGradient>
    </defs>
    <rect width="1200" height="996" fill="url(#scene)" role="img" aria-label="Photo of a large rooftop solar panel array with trees and brick buildings behind"/>
    <polygon points="800,0 1200,0 1200,150 960,150" fill="#ffffff" opacity="0.25"/>
    <polygon points="0,0 640,0 0,720" fill="url(#blueLeft)"/>
    <polygon points="0,0 420,0 0,470" fill="#1fc0ee" opacity="0.35"/>
    <polygon points="40,0 260,0 180,140" fill="#ffffff" opacity="0.12"/>
    <polygon points="480,0 560,0 350,190" fill="#ffffff" opacity="0.12"/>
    <g stroke="#3bc6ee" stroke-width="7" opacity="0.55" fill="none">
      <line x1="420" y1="50" x2="40" y2="420"/>
      <line x1="480" y1="60" x2="70" y2="440"/>
      <line x1="640" y1="150" x2="0" y2="760"/>
      <line x1="680" y1="170" x2="0" y2="810"/>
    </g>
    <polygon points="860,0 920,0 380,996 320,996" fill="var(--teal-band)" opacity="0.75"/>
    <polygon points="950,0 985,0 450,996 415,996" fill="var(--teal-band)" opacity="0.6"/>
    <polygon points="1060,0 1200,0 1200,40 650,996 560,996" fill="#ffffff" opacity="0.18"/>
    <polygon points="1200,90 1200,140 700,996 650,996" fill="var(--teal-band)" opacity="0.7"/>
    <polygon points="1200,200 1200,240 760,996 720,996" fill="var(--teal-band)" opacity="0.6"/>
    <polygon points="1200,400 1200,996 620,996" fill="url(#blueRight)" opacity="0.92"/>
    <polygon points="0,740 120,640 60,996 0,996" fill="#ffffff" opacity="0.15"/>
  </svg>

  <h1 class="heading">PRODUCTS WE OFFER</h1>

  <ul class="products">
    <li class="product product--inverters"><span class="product__thumb"><span role="img" aria-label="Photo of solar inverter units on a wall" style="background:linear-gradient(135deg,#6b6f86,#e9a46a)"></span></span>Solar Inverters</li>
    <li class="product product--batteries"><span class="product__thumb"><span role="img" aria-label="Photo of a solar battery cell module" style="background:linear-gradient(135deg,#1e2a44,#3a5a8a)"></span></span>Solar Batteries</li>
    <li class="product product--panels"><span class="product__thumb"><span role="img" aria-label="Photo of a field of solar panels" style="background:linear-gradient(180deg,#9fb1c9,#3b4866)"></span></span>Solar Panels</li>
  </ul>

  <section class="services">
    <div class="service__photo" role="img" aria-label="Photo of a cleaning pole washing solar panels" style="left:664px;top:104px;background:linear-gradient(135deg,#aebfd8,#2d4d93)"></div>
    <p class="service__label" style="left:828px;top:120px;width:220px;">System<br>Maintenance<br>&amp; Cleaning</p>

    <div class="service__photo" role="img" aria-label="Photo of hands testing a solar panel connection" style="left:488px;top:286px;background:linear-gradient(135deg,#3a63b5,#c9a28a)"></div>
    <p class="service__label" style="left:648px;top:304px;width:215px;">Solar System<br>Monitoring</p>

    <div class="service__photo" role="img" aria-label="Photo of a technician in a hard hat installing solar panels" style="left:298px;top:482px;background:linear-gradient(180deg,#5fa0dc,#2f3f6a)"></div>
    <p class="service__label" style="left:462px;top:500px;width:205px;">Solar I<br>Nstallation<br>Auditing</p>

    <div class="service__photo" role="img" aria-label="Photo of a laptop and multimeter on solar panels" style="left:200px;top:716px;background:linear-gradient(135deg,#5a6fa8,#2a3350)"></div>
    <p class="service__label" style="left:360px;top:738px;width:215px;">Maintenance<br>Schedules</p>
  </section>

  <section class="testimonial">
    <div class="client-photo"><span role="img" aria-label="Photo of a wet car bonnet"></span></div>
    <h2 class="testimonial__name">Corvale Motors</h2>
    <p class="testimonial__quote">Marcus was completely professional and refreshingly reliable at every stage. I would and have recommended Marcus for any job, large or small</p>
  </section>
</main>
</body>
</html>
```